Letterhead design for Sleep Consulting Business

I'm looking for a new letterhead (heading/footer) design for my Sleep Consulting Business, I work with families to help their children improve their sleep.

The heading/footer will used in Microsoft Word Only-to be used for all of my documents such as writing Sleep Plans. I need to utilize as much working space in the document as possible. This will NOT be printed out on paper- it will only be used for heading/footer on microsoft word, then emailed to clients, who may print it at home.

My brand colors:
Dark Blue Hex: 1F2A42
Lighter Blueish Hex: 90BEC9
You're welcome to check out my website for inspiration- it is freshly created with other colors as well, and I love the outcome. www.hollowpinerest.com

Target Market(s)

Tired parents

Font styles to use
Script
Other font styles liked:
• Great Vibe, Lato or Just Another Hand are all used currently for my brand. Open to other options.

Requirements
Must have
• The letterhead (heading/footer) MUST be kept narrow (height-wise), so I have plenty of space on my document, while including important information.

It should look professional on screen, and when printed.

Must include my business name OR logo (Hollow Pine Sleep Consulting), and my email address. Mara@hollowpinerest.com

Website is optional, not required, just if you need to fill in a spot: www.hollowpinerest.com

```html
<!DOCTYPE html>
<html lang="en">
<head>
<meta charset="utf-8">
<title>Hollow Pine Sleep Consulting — Letterhead</title>
<link rel="stylesheet" href="https://fonts.googleapis.com/css2?family=Lato:wght@400;700&display=swap">
<style>
  :root {
    --navy: #1F2A42;
    --mist: #90BEC9;
    --ink: #4a4d55;
    --paper: #ffffff;
    --backdrop: #ecedef;
  }
  * { margin: 0; padding: 0; box-sizing: border-box; }
  html, body {
    width: 1200px; height: 936px; overflow: hidden;
    background: var(--backdrop);
    font-family: "Lato", Arial, sans-serif;
    color: var(--ink);
  }
  .letterhead {
    position: absolute; left: 289px; top: 28px;
    width: 622px; height: 880px;
    background: var(--paper);
    box-shadow: 0 4px 18px rgba(0,0,0,.12);
    overflow: hidden;
  }

  /* Header */
  .brand {
    position: absolute; left: 34px; top: 96px;
    display: flex; align-items: center; gap: 10px;
  }
  .brand-dot {
    width: 34px; height: 34px; border-radius: 50%;
    background: var(--mist);
  }
  .brand-name {
    font-size: 15px; font-weight: 400; color: var(--navy);
    letter-spacing: .2px;
  }
  .rule-navy, .rule-mist {
    position: absolute; left: 0; width: 622px;
  }
  .header-rule.rule-navy { top: 146px; height: 4px; background: var(--navy); }
  .header-rule.rule-mist { top: 153px; height: 3px; background: var(--mist); }

  /* Letter body */
  .letter {
    position: absolute; left: 70px; top: 190px; width: 490px;
    font-size: 11px; line-height: 1.45;
  }
  .date { margin-bottom: 10px; }
  .recipient { margin-bottom: 12px; }
  .salutation { font-weight: 700; margin-bottom: 14px; }
  .letter p.body { margin-bottom: 14px; }
  .closing { margin-top: 22px; }
  .signature {
    width: 90px; height: 26px; margin-top: 6px;
    background: linear-gradient(90deg, rgba(31,42,66,.35), rgba(31,42,66,.1));
    border-radius: 3px;
  }

  /* Footer */
  .footer-brand {
    position: absolute; right: 34px; top: 762px;
    display: flex; align-items: center; gap: 8px;
  }
  .footer-brand .brand-dot { width: 22px; height: 22px; }
  .footer-brand .brand-name { font-size: 11px; }
  .footer-rule.rule-mist { top: 796px; height: 3px; background: var(--mist); }
  .footer-rule.rule-navy { top: 802px; height: 4px; background: var(--navy); }
  .contact {
    position: absolute; left: 40px; top: 818px;
    font-size: 10.5px; color: var(--navy); line-height: 1.6;
  }
  .contact li { list-style: none; display: flex; align-items: center; gap: 6px; }
  .contact svg { width: 10px; height: 10px; }
</style>
</head>
<body>
<main class="letterhead">
  <header class="brand">
    <span class="brand-dot"></span>
    <span class="brand-name">Hollow Pine Sleep Consulting</span>
  </header>
  <div class="header-rule rule-navy"></div>
  <div class="header-rule rule-mist"></div>

  <section class="letter">
    <p class="date">January 12, 2012</p>
    <p class="recipient">Mr. John Doe<br>President<br>AA Corporation<br>111 Street Name, Suite#<br>City, State, 12345</p>
    <p class="salutation">Dear Mr. John,</p>
    <p class="body">Lorem Ipsum is simply dummy text of the printing and typesetting industry. Lorem Ipsum has been the industry's standard dummy text ever since the 1500s, when an unknown printer took a galley of type and scrambled it to make a type specimen book. It has survived not only five centuries, but also the leap into electronic typesetting, remaining essentially unchanged.</p>
    <p class="body">The standard chunk of Lorem Ipsum used since the 1500s is reproduced below for those interested. Sections 1.10.32 and 1.10.33 from "de Finibus Bonorum et Malorum" by Tullan are also reproduced in their exact original form, accompanied by English versions from the 1914 translation by H. Marlow.</p>
    <p class="body">Lorem Ipsum is simply dummy text of the printing and typesetting industry. Lorem Ipsum has been the industry's standard dummy text ever since the 1500s, when an unknown printer took a galley of type and scrambled it to make a type specimen book. It has survived not only five centuries, but also the leap into electronic typesetting, remaining essentially unchanged. It was popularised in the</p>
    <p class="closing">Sincerely Your,</p>
    <div class="signature" role="img" aria-label="Handwritten signature"></div>
  </section>

  <footer>
    <div class="footer-brand">
      <span class="brand-dot"></span>
      <span class="brand-name">Hollow Pine Sleep Consulting</span>
    </div>
    <div class="footer-rule rule-mist"></div>
    <div class="footer-rule rule-navy"></div>
    <ul class="contact">
      <li><svg viewBox="0 0 10 10" aria-hidden="true"><circle cx="5" cy="5" r="5" fill="var(--navy)"/><rect x="2.5" y="3.2" width="5" height="3.6" fill="none" stroke="#fff" stroke-width=".8"/></svg>Mara@hollowpinerest.com</li>
      <li><svg viewBox="0 0 10 10" aria-hidden="true"><circle cx="5" cy="5" r="5" fill="var(--navy)"/><circle cx="5" cy="5" r="2.6" fill="none" stroke="#fff" stroke-width=".8"/></svg>www.hollowpinerest.com</li>
    </ul>
  </footer>
</main>
</body>
</html>
```